Business card

We need a business card design for our company based in Auckland , New Zealand called 'Kestrel + Design Ltd'. We provide architectural services. We would like to see designs that use the max. three colours (such as white, black, grey) The final design should communicate financial safety and growth."
Also I will provide our company logo. I would like to the logo to be embeded onto our business card.

Target Market(s)

new residential house, alteration & addition & light commericila design & drafting service

Industry/Entity Type

Architecture

Contact Information for Business Card

Company name: kestrel + design Ltd.
Name: Mark Telford
Job title: architectural designer & Design RQC
email address: mark@kdstudio.co.nz
mobile number: 02 5319 6620
web site: www.kdstudio.co.nz

Requirements
Must have
• My project must have..
• - embeded logo (attached company logo)
• I don't have a bigger version for our company logo, but I have one old one, so you can remove the word from it)
• - insert the attached small PDGQ logo & RQC logo
• - creative, simple and clear business card.
• - Max. three colours
Nice to have
• - Here are the samples I would like to share with you: http://www.velmorindex.com/blog/minimalistic-business-card-designs/
• I would like to have my business card like one of the creation.
Should not have
• TBA

```html
<!DOCTYPE html>
<html lang="en">
<head>
<meta charset="utf-8">
<title>Kestrel + Design Ltd — Business Card</title>
<link rel="stylesheet" href="https://fonts.googleapis.com/css2?family=Lato:wght@300;400;700&display=swap">
<style>
  :root {
    --bg: #1c1c1c;
    --card: #262626;
    --white: #f2f2f2;
    --grey: #8d8d8d;
    --rule: #4a4a4a;
    --accent: #e24f26;
  }
  * { margin: 0; padding: 0; box-sizing: border-box; }
  html, body {
    width: 1200px; height: 900px; overflow: hidden;
    background: var(--bg);
    font-family: "Lato", Arial, sans-serif;
  }
  .canvas {
    position: relative; width: 1200px; height: 900px;
    display: flex; justify-content: center; align-items: center; gap: 120px;
  }
  .card {
    position: relative; width: 340px; height: 550px;
    background: var(--card);
    box-shadow: 0 10px 30px rgba(0,0,0,.35);
  }
  .company-name {
    position: absolute; left: 0; right: 0; text-align: center;
    color: var(--white); font-weight: 400; font-size: 16px;
    letter-spacing: .2em; text-transform: uppercase;
  }
  .card--back .company-name { top: 212px; }
  .card--front .company-name { top: 92px; }
  .card__footer {
    position: absolute; left: 0; right: 0; bottom: 30px; height: 62px;
    border-top: 1px solid var(--rule);
    border-bottom: 1px solid var(--rule);
    display: flex; align-items: center; justify-content: center;
  }
  .website--footer {
    color: var(--grey); font-size: 14px; letter-spacing: .16em;
    text-transform: uppercase;
  }
  .contact {
    position: absolute; top: 205px; left: 0; right: 0; text-align: center;
    text-transform: uppercase;
  }
  .contact__name {
    color: var(--white); font-size: 21px; font-weight: 400; letter-spacing: .18em;
  }
  .contact__role {
    color: var(--accent); font-size: 11.5px; font-weight: 400; letter-spacing: .1em;
    margin-top: 4px;
  }
  .contact__lines {
    list-style: none; margin-top: 12px;
    color: var(--white); font-size: 13px; letter-spacing: .14em; line-height: 1.5;
  }
  .memberships {
    position: absolute; left: 44px; bottom: 50px; display: flex; gap: 16px; align-items: center;
  }
  .badge { display: block; }
</style>
</head>
<body>
<main class="canvas">
  <section class="card card--back" aria-label="Business card back">
    <p class="company-name">Kestrel + Design Ltd.</p>
    <div class="card__footer">
      <span class="website--footer">www.kdstudio.co.nz</span>
    </div>
  </section>

  <section class="card card--front" aria-label="Business card front">
    <p class="company-name">Kestrel + Design Ltd.</p>
    <div class="contact">
      <h1 class="contact__name">Mark Telford</h1>
      <p class="contact__role">Architectural Designer &amp; Design RQC</p>
      <ul class="contact__lines">
        <li>mark@kdstudio.co.nz</li>
        <li>02 5319 6620</li>
        <li>www.kdstudio.co.nz</li>
      </ul>
    </div>
    <div class="memberships">
      <svg class="badge" width="34" height="34" viewBox="0 0 34 34" role="img" aria-label="RQC licence badge">
        <circle cx="17" cy="17" r="16" fill="var(--white)"/>
      </svg>
      <svg class="badge" width="34" height="34" viewBox="0 0 34 34" role="img" aria-label="PDGQ professional member badge">
        <rect x="2" y="2" width="30" height="30" fill="var(--white)"/>
      </svg>
    </div>
  </section>
</main>
</body>
</html>
```